A simple Chatterbook Ad (not Chatterbook Page) for weight loss surgery

It’s a simple ad in terms of the text.

The text should say:
Curious about weight loss surgery?
This 30 second quiz will tell you which procedure will suit you best

I'm open to variations in the text if it is thought to enhance the ad.

Targeted towards obese individuals who have been unable to lose weight with diet and exercise. My industry is weight loss surgery – webpage www.marcusbellweather.com.au. Clicking the ad leads to a quiz on my webpage relating to weight loss surgery. Most frequent users of this service are females (75%) between ages of 35 and 55 years.

Successful weight loss surgery can enable individuals who have been unable to lose weight to lose a substantial amount of the excess weight they are carrying to be healthier and happier.

```html
<!DOCTYPE html>
<html lang="en">
<head>
<meta charset="utf-8">
<title>Weight Loss Surgery Quiz Ads</title>
<link rel="stylesheet" href="https://fonts.googleapis.com/css2?family=Marcellus&family=Montserrat:ital,wght@0,700;0,800;1,800&display=swap">
<style>
:root{
  --sheet:#232323;
  --wall:#c9cdcd;
  --ad-bg:#252525;
  --teal:#0e8c82;
  --teal-deep:#0b5f59;
  --teal-text:#13998d;
  --white:#ffffff;
  --footer-grey:#454545;
  --photo-dark:#1d3b3d;
  --photo-mid:#1f5a60;
  --photo-blue:#2c6d86;
}
*{margin:0;padding:0;box-sizing:border-box}
html,body{width:1200px;height:1027px;overflow:hidden;background:var(--sheet)}
.sheet{position:relative;width:1200px;height:1027px;background:var(--sheet)}
.wall-edge{position:absolute;left:1139px;top:0;width:61px;height:1027px;background:var(--wall)}
.ad{position:absolute;background:var(--ad-bg);overflow:hidden}
.photo{position:absolute}
.frame{position:absolute;border:4px solid var(--teal)}
.serif{font-family:"Marcellus",serif;position:absolute;white-space:nowrap;line-height:1}
.curious{color:var(--white)}
.weight-loss{color:var(--teal-text)}
.surgery{color:var(--white)}
.dial{position:absolute}
.dial-count{position:absolute;font-family:"Montserrat",sans-serif;font-weight:800;color:var(--teal-text);line-height:1;white-space:nowrap}
.dial-count small{font-size:45%}
.pitch{position:absolute;font-family:"Montserrat",sans-serif;font-weight:700;color:var(--white);line-height:1.22;letter-spacing:.5px;text-transform:uppercase}
.pitch em{font-style:normal;color:var(--teal-text)}
.cta{position:absolute;border-radius:999px;border:2px solid #e9eded;
  background:linear-gradient(#f4f4f4 0%,#b8b8b8 30%,#7a7a7a 55%,#5b5b5b 75%,#9a9a9a 100%);
  box-shadow:0 2px 6px rgba(0,0,0,.6);
  display:flex;align-items:center;justify-content:center;
  font-family:"Montserrat",sans-serif;font-style:italic;font-weight:800;color:var(--white);
  text-shadow:0 1px 3px rgba(0,0,0,.7)}
.footer{position:absolute;left:0;right:0;bottom:0}
.footer-teal{position:absolute;left:0;top:0;bottom:0;background:var(--teal-deep)}
.footer-grey{position:absolute;top:0;bottom:0;right:0;background:var(--footer-grey)}
.url{position:absolute;font-family:"Montserrat",sans-serif;font-weight:700;color:var(--white);font-size:11.5px;letter-spacing:2px;white-space:nowrap;text-align:right}
.brand{position:absolute;display:flex;align-items:center;gap:8px}
.brand-dot{width:30px;height:30px;border-radius:50%;background:var(--teal)}
.brand-name{font-family:"Marcellus",serif;color:var(--teal-text);font-size:19px;line-height:1;white-space:nowrap}
.brand-role{font-family:"Marcellus",serif;color:#9aa0a0;font-size:6.5px;letter-spacing:1px;line-height:1.4;white-space:nowrap}
.size-label{position:absolute;font-family:"Montserrat",sans-serif;font-weight:700;color:var(--white);font-size:32px;transform:translateX(-50%);white-space:nowrap}
</style>
</head>
<body>
<main class="sheet">
  <div class="wall-edge"></div>

  <!-- Story format -->
  <section class="ad ad-story" style="left:64px;top:49px;width:504px;height:888px">
    <div class="photo" role="img" aria-label="Surgical team working in an operating theatre" style="left:0;top:420px;width:504px;height:468px;background:linear-gradient(180deg,var(--ad-bg) 0%,var(--photo-dark) 30%,var(--photo-mid) 65%,var(--photo-blue) 100%)"></div>
    <div class="frame" style="left:9px;top:2px;right:9px;bottom:48px"></div>

    <div class="brand" style="left:140px;top:40px">
      <span class="brand-dot"></span>
      <div><div class="brand-name">Marcus Bellweather</div><div class="brand-role">GENERAL, UPPER GI &amp; BARIATRIC SURGEON</div></div>
    </div>

    <div class="serif curious" style="left:0;width:504px;text-align:center;top:106px;font-size:35px">Curious about</div>
    <div class="serif weight-loss" style="left:0;width:504px;text-align:center;top:146px;font-size:64px">WEIGHT LOSS</div>
    <div class="serif surgery" style="left:0;width:504px;text-align:center;top:218px;font-size:61px">SURGERY?</div>

    <svg class="dial" viewBox="0 0 300 300" style="left:132px;top:305px;width:270px;height:270px" aria-hidden="true">
      <circle cx="150" cy="150" r="136" fill="none" stroke="var(--white)" stroke-width="22" pathLength="600" stroke-dasharray="3.5 6.5" stroke-dashoffset="1.75" transform="rotate(-90 150 150)"/>
      <circle cx="150" cy="150" r="136" fill="none" stroke="var(--teal-text)" stroke-width="22" pathLength="600" stroke-dasharray="3.5 6.5 3.5 6.5 3.5 576.5" stroke-dashoffset="11.75" transform="rotate(-90 150 150)"/>
    </svg>
    <div class="dial-count" style="left:132px;width:270px;text-align:center;top:405px;font-size:68px">30<small>s</small></div>

    <p class="pitch" style="left:0;width:504px;text-align:center;top:597px;font-size:21px">This <em>30 second quiz</em> will<br>tell you which procedure<br>will suit you best</p>

    <div class="cta" style="left:122px;top:720px;width:259px;height:59px;font-size:24px">CLICK HERE</div>

    <div class="footer" style="height:50px">
      <div class="footer-teal" style="width:170px;clip-path:polygon(0 0,100% 0,50% 100%,0 100%)"></div>
      <div class="footer-grey" style="left:110px;clip-path:polygon(45px 0,100% 0,100% 100%,0 100%)"></div>
      <div class="url" style="right:22px;top:18px">WWW.MARCUSBELLWEATHER.COM.AU/</div>
    </div>
  </section>
  <div class="size-label" style="left:307px;top:956px">1080X1920</div>

  <!-- Square format -->
  <section class="ad ad-square" style="left:596px;top:56px;width:529px;height:522px">
    <div class="photo" role="img" aria-label="Surgical team working in an operating theatre" style="left:0;top:180px;width:529px;height:342px;background:linear-gradient(160deg,var(--ad-bg) 0%,var(--photo-dark) 35%,var(--photo-mid) 70%,var(--photo-blue) 100%)"></div>
    <div class="frame" style="left:12px;top:1px;right:11px;bottom:47px"></div>

    <div class="serif curious" style="left:0;width:529px;text-align:center;top:22px;font-size:34px">Curious about</div>
    <div class="serif weight-loss" style="left:0;width:529px;text-align:center;top:60px;font-size:64px">WEIGHT LOSS</div>
    <div class="serif surgery" style="left:0;width:529px;text-align:center;top:114px;font-size:61px">SURGERY?</div>

    <svg class="dial" viewBox="0 0 300 300" style="left:-3px;top:175px;width:270px;height:270px" aria-hidden="true">
      <circle cx="150" cy="150" r="136" fill="none" stroke="var(--white)" stroke-width="22" pathLength="600" stroke-dasharray="3.5 6.5" stroke-dashoffset="1.75" transform="rotate(-90 150 150)"/>
      <circle cx="150" cy="150" r="136" fill="none" stroke="var(--teal-text)" stroke-width="22" pathLength="600" stroke-dasharray="3.5 6.5 3.5 6.5 3.5 576.5" stroke-dashoffset="11.75" transform="rotate(-90 150 150)"/>
    </svg>
    <div class="dial-count" style="left:-3px;width:270px;text-align:center;top:275px;font-size:68px">30<small>s</small></div>

    <p class="pitch" style="left:280px;top:214px;font-size:20.5px">This <em>30 second<br>quiz</em> will tell<br>you which<br>procedure will<br>suit you best!</p>

    <div class="cta" style="left:250px;top:372px;width:245px;height:56px;font-size:22px">CLICK HERE</div>

    <div class="footer" style="height:47px">
      <div class="footer-teal" style="width:160px;clip-path:polygon(0 0,100% 0,50% 100%,0 100%)"></div>
      <div class="footer-grey" style="left:90px;clip-path:polygon(45px 0,100% 0,100% 100%,0 100%)"></div>
      <div class="url" style="right:24px;top:17px">WWW.MARCUSBELLWEATHER.COM.AU/</div>
    </div>
  </section>
  <div class="size-label" style="left:871px;top:589px">1080X1080</div>

  <!-- Landscape format -->
  <section class="ad ad-wide" style="left:599px;top:646px;width:528px;height:277px">
    <div class="photo" role="img" aria-label="Surgical team working in an operating theatre" style="left:150px;top:0;width:378px;height:277px;background:linear-gradient(100deg,var(--ad-bg) 0%,var(--photo-dark) 45%,var(--photo-mid) 80%,var(--photo-blue) 100%)"></div>
    <div class="frame" style="left:12px;top:8px;right:7px;bottom:9px"></div>

    <div class="serif curious" style="left:29px;top:22px;font-size:31px">Curious about</div>
    <div class="serif weight-loss" style="left:28px;top:52px;font-size:56px">WEIGHT LOSS</div>
    <div class="serif surgery" style="left:28px;top:98px;font-size:54px">SURGERY?</div>

    <div class="cta" style="left:326px;top:118px;width:181px;height:41px;font-size:16px">CLICK HERE</div>

    <div style="position:absolute;left:0;top:170px;width:245px;height:78px;background:var(--teal-deep);clip-path:polygon(0 0,100% 0,72% 100%,0 100%)"></div>
    <div style="position:absolute;left:217px;top:170px;width:311px;height:78px;background:var(--footer-grey);clip-path:polygon(28px 0,100% 0,100% 100%,0 100%)"></div>

    <svg class="dial" viewBox="0 0 300 300" style="left:79px;top:154px;width:108px;height:108px" aria-hidden="true">
      <circle cx="150" cy="150" r="133" fill="none" stroke="var(--white)" stroke-width="26" pathLength="600" stroke-dasharray="3.5 6.5" stroke-dashoffset="1.75" transform="rotate(-90 150 150)"/>
      <circle cx="150" cy="150" r="133" fill="none" stroke="var(--teal-text)" stroke-width="26" pathLength="600" stroke-dasharray="3.5 6.5 3.5 6.5 3.5 576.5" stroke-dashoffset="11.75" transform="rotate(-90 150 150)"/>
    </svg>
    <div class="dial-count" style="left:79px;width:108px;text-align:center;top:194px;font-size:26px">30<small>s</small></div>

    <p class="pitch" style="left:312px;top:175px;font-size:13.5px;line-height:1.25">This <em>30 second quiz</em><br>will tell you which<br>procedure will<br>suit you best!</p>
  </section>
  <div class="size-label" style="left:871px;top:930px">120X628</div>
</main>
</body>
</html>
```